Update the A4 Specials Page for Restaurant/Cafe

Provide a MINIMALIST attractive Specials page we can print weekly for our food and drink specials to give to our guests. Final design is to be provided in WORD Document so it can be easily edited by Manager. Should be black text and MINIMALIST to minimise ink usage as we print hundreds a week. We have UPLOADED the existing page as a template for you to update. Maybe logo can stay, see what you think. Or delete it and do something else. Keep it simple. Choose a good FONT. Could be a little playful with a cocktail ICON or something. Our existing menus can be seen at www.tallowmillcafe.com.au and they are using font Alegreya. Please note we are unable to provide any feedback to designers, however we really do appreciate your time if you are submitting a design. Thank you for your participation.

```html
<!DOCTYPE html>
<html lang="en">
<head>
<meta charset="UTF-8">
<title>Tallow Mill Cafe – Weekly Specials</title>
<link rel="stylesheet" href="https://fonts.googleapis.com/css2?family=Bebas+Neue&family=Montserrat:wght@500;600;700;800&display=swap">
<style>
  :root {
    --paper: #ffffff;
    --ink: #111111;
    --sketch-area: #fcfcfc;
  }
  * { margin: 0; padding: 0; box-sizing: border-box; }
  html, body {
    width: 920px; height: 1200px; overflow: hidden;
    background: var(--paper);
    font-family: "Montserrat", Arial, sans-serif;
    color: var(--ink);
  }
  .page {
    position: relative;
    width: 920px; height: 1200px;
    background: var(--paper);
    overflow: hidden;
  }
  .sketch {
    position: absolute; top: 44px; width: 215px; height: 1100px;
    background: var(--sketch-area);
  }
  .sketch--left { left: 0; }
  .sketch--right { right: 0; }
  .line {
    position: absolute; left: 0; right: 0;
    text-align: center; white-space: nowrap;
    color: var(--ink);
  }
  .brand {
    top: 44px;
    font-weight: 800; font-size: 40px; line-height: 48px;
    letter-spacing: 1px; text-transform: uppercase;
  }
  .section-title {
    top: 241px;
    font-family: "Bebas Neue", Impact, sans-serif;
    font-size: 50px; line-height: 50px; font-weight: 400;
  }
  .dish-name {
    font-weight: 600; font-size: 30px; line-height: 36px;
    text-transform: uppercase; letter-spacing: 0.3px;
  }
  .detail {
    font-weight: 600; font-size: 17px; line-height: 20px;
  }
  .price { font-weight: 700; font-size: 29px; line-height: 32px; }
</style>
</head>
<body>
  <main class="page">
    <div class="sketch sketch--left" role="img" aria-label="Faint line drawings of cocktails, fruit and mint leaves"></div>
    <div class="sketch sketch--right" role="img" aria-label="Faint line drawings of cocktails, fruit and mint leaves"></div>

    <div class="line brand">Tallow Mill<br>Cafe</div>

    <h1 class="line section-title">Weekly Specials</h1>

    <h2 class="line dish-name" style="top:300px">Chicken Filo</h2>
    <p class="line detail" style="top:340px">Creamy Chicken with Pinenuts,</p>
    <p class="line detail" style="top:359px">wrapped in Filo Pastry.</p>
    <p class="line detail" style="top:392px">Served with Side Salad &amp; Zulu Sauce</p>
    <p class="line price" style="top:423px">$24</p>

    <h2 class="line dish-name" style="top:526px">Minestrone Soup</h2>
    <p class="line detail" style="top:568px">Served with Garlic Bread</p>
    <p class="line price" style="top:601px">$8</p>

    <h2 class="line dish-name" style="top:697px">Cocktail Special</h2>
    <p class="line detail" style="top:739px">PASSIONISTA</p>
    <p class="line detail" style="top:770px">Vodka, Passionfruit Pulp, Mango Puree</p>
    <p class="line detail" style="top:796px">Top up with Ginger &amp; Lemon Kombucha</p>
    <p class="line price" style="top:823px">$17</p>

    <h2 class="line dish-name" style="top:913px">Craft Beer Special</h2>
    <p class="line detail" style="top:954px">CROOKED GECKO</p>
    <p class="line detail" style="top:978px">SUN BURST</p>
    <p class="line detail" style="top:1001px">Tropical Pale Ale</p>
    <p class="line detail" style="top:1024px">4.8% Alc.</p>
    <p class="line price" style="top:1074px">$10</p>
  </main>
</body>
</html>
```